PTA Meeting Poster

We are looking to create a poster to invite parents of our school to our monthly PTA Meeting.

The copy should include:

PTA Meeting
This Wednesday
8:40am
in the Multi Purpose Room

All Welcome!

```html
<!DOCTYPE html>
<html lang="en">
<head>
<meta charset="utf-8">
<title>PTA Meeting Poster</title>
<link rel="stylesheet" href="https://fonts.googleapis.com/css2?family=Crimson+Pro:wght@700&family=Cormorant+SC:wght@700&family=Great+Vibes&display=swap">
<style>
  :root {
    --frame-purple: #7a2bc9;
    --panel-light: #ffff66;
    --panel-gold: #ffcc00;
    --headline-red: #ff0000;
    --details-green: #006600;
  }
  html, body {
    margin: 0;
    padding: 0;
    overflow: hidden;
    background: #ffffff;
  }
  .poster {
    position: relative;
    width: 1200px;
    height: 890px;
    overflow: hidden;
  }
  .poster__backdrop {
    position: absolute;
    inset: 0;
    display: block;
  }
  .poster__title {
    position: absolute;
    left: 0;
    right: 0;
    top: 88px;
    margin: 0;
    text-align: center;
    font-family: "Crimson Pro", Georgia, serif;
    font-weight: 700;
    font-size: 160px;
    line-height: 1;
    color: var(--headline-red);
    letter-spacing: 1px;
  }
  .poster__details {
    position: absolute;
    left: 0;
    right: 0;
    top: 310px;
    margin: 0;
    text-align: center;
    font-family: "Cormorant SC", Georgia, serif;
    font-weight: 700;
    font-size: 72px;
    line-height: 73px;
    color: var(--details-green);
    letter-spacing: 1px;
  }
  .poster__details span {
    display: block;
  }
  .poster__welcome {
    position: absolute;
    left: 128px;
    top: 690px;
    margin: 0;
    font-family: "Great Vibes", cursive;
    font-size: 124px;
    line-height: 1;
    color: var(--headline-red);
  }
</style>
</head>
<body>
  <main class="poster">
    <svg class="poster__backdrop" width="1200" height="890" viewBox="0 0 1200 890" aria-hidden="false">
      <rect class="frame" x="0" y="0" width="1200" height="890" fill="var(--frame-purple)" role="img" aria-label="Checkered border in purple, yellow and tan squares"/>
      <rect class="frame-inner-line" x="52" y="52" width="1096" height="786" fill="var(--panel-light)"/>
      <rect class="panel" x="59" y="59" width="1082" height="772" fill="var(--panel-gold)"/>
      <path class="panel-wave" fill="var(--panel-light)"
        d="M59,327 C237,247 427,228 607,280 C806,327 996,323 1141,294
           L1141,673 C1000,720 800,720 664,664 C540,610 330,600 59,740 Z"/>
    </svg>

    <h1 class="poster__title">PTA Meeting</h1>

    <p class="poster__details">
      <span>This Wednesday</span>
      <span>8:40am</span>
      <span>in the</span>
      <span>Multi Purpose Room</span>
    </p>

    <p class="poster__welcome">All Welcome!</p>
  </main>
</body>
</html>
```